【依頼の目的/概要】
電子書籍(lumora)の表紙デザインをお願いします。

【画像サイズ】 ※RZBより抜粋
表紙ファイルの理想的な寸法 2,560×1,600ピクセルです。
注:画像の寸法は 1,000×625ピクセル以上であることが必要です。
画像の最大の寸法は 10,000×10,000ピクセルです。

【タイトル】

5つの航路・ヴォルテノ大年譜など
人類普遍の必読真理書をギュっと1冊にまとめました

【著者】

RUNO

【本の内容】

5つの航路・ヴォルテノ大年譜などの人間心理・成功本を
まとめて解説した本です。

※本文を参考資料として添付します。

【デザイン要望】

特にイメージにこだわりはありませんので、
自由な発送でのデザインご応募を楽しみにしています。

※次点の方への参加報酬を設定致しました。

※その他 必要な情報がありましたら、お問い合わせください。

```html
<!DOCTYPE html>
<html lang="ja">
<head>
<meta charset="utf-8">
<title>5つの航路 — 表紙</title>
<link href="https://fonts.googleapis.com/css2?family=Noto+Serif+JP:wght@500;700;900&display=swap" rel="stylesheet">
<style>
  :root {
    --ink-dark: #1c1a2a;
    --navy: #22243f;
    --red: #b0161c;
    --white: #ffffff;
    --gold-1: #3a2a14;
    --gold-2: #8a6a34;
    --shadow: rgba(0,0,0,0.75);
  }
  html, body { margin: 0; padding: 0; overflow: hidden; background: #111; }
  .cover {
    position: relative;
    width: 750px; height: 1200px;
    overflow: hidden;
    font-family: "Noto Serif JP", serif;
    color: var(--white);
  }
  .cover-photo {
    position: absolute; inset: 0;
    background:
      radial-gradient(ellipse 40% 30% at 55% 35%, rgba(220,200,150,0.5), transparent 70%),
      radial-gradient(ellipse 70% 60% at 50% 45%, var(--gold-2), transparent 75%),
      linear-gradient(180deg, #2a1f12 0%, var(--gold-1) 45%, #1a130b 100%);
  }
  .abs { position: absolute; margin: 0; line-height: 1; white-space: nowrap; }
  .lead { text-shadow: 0 2px 6px var(--shadow); font-weight: 700; }
  .lead-ruby { left: 190px; top: 26px; font-size: 16px; font-weight: 500; }
  .lead-1 { left: 22px; top: 48px; font-size: 36px; }
  .lead-2 { left: 145px; top: 92px; font-size: 36px; }
  .label {
    background: var(--white); color: var(--ink-dark);
    font-weight: 900; padding: 8px 14px; box-shadow: 0 3px 10px var(--shadow);
  }
  .label-1 { left: 20px; top: 160px; font-size: 34px; }
  .label-1-tail { left: 318px; top: 186px; font-size: 18px; font-weight: 700; text-shadow: 0 2px 6px var(--shadow); }
  .label-2 { left: 20px; top: 230px; font-size: 34px; }
  .lead-3 { left: 75px; top: 325px; font-size: 22px; }
  .title { font-weight: 900; text-shadow: 0 4px 18px var(--shadow), 0 0 3px #000; }
  .title-num { left: 385px; top: 40px; font-size: 330px; }
  .title-tsu { left: 495px; top: 280px; font-size: 95px; }
  .title-no { left: 470px; top: 375px; font-size: 115px; }
  .title-k1 { left: 75px; top: 345px; font-size: 250px; }
  .title-k2 { left: 75px; top: 585px; font-size: 250px; }
  .lead-4 { left: 25px; top: 820px; font-size: 58px; font-weight: 900; text-shadow: 0 3px 10px var(--shadow); }
  .role { left: 478px; top: 852px; font-size: 19px; font-weight: 500; text-shadow: 0 2px 6px var(--shadow); }
  .author { left: 505px; top: 885px; font-size: 52px; font-weight: 700; letter-spacing: 2px; text-shadow: 0 2px 8px var(--shadow); }
  .band {
    position: absolute; left: 0; right: 0; top: 955px; bottom: 0;
    background: linear-gradient(180deg, rgba(255,255,255,0.8), var(--white) 18%);
  }
  .red { color: var(--red); font-weight: 900; }
  .navy { color: var(--navy); font-weight: 900; }
  .big-life { left: 22px; top: 935px; font-size: 125px; text-shadow: 0 0 6px #fff; }
  .tail-1 { left: 300px; top: 985px; font-size: 44px; }
  .trouble { left: 148px; top: 1055px; font-size: 36px; }
  .big-essence { left: 468px; top: 1025px; font-size: 112px; }
  .tail-2 { left: 505px; top: 1133px; font-size: 44px; }
  .gift-tag {
    position: absolute; left: 12px; top: 1108px; width: 42px; height: 78px;
    background: var(--red); color: var(--white);
    writing-mode: vertical-rl; font-size: 13px; font-weight: 700;
    display: flex; align-items: center; justify-content: center; line-height: 1.15;
  }
  .gift-text { left: 66px; top: 1122px; font-size: 20px; line-height: 1.35; color: var(--navy); font-weight: 700; }
</style>
</head>
<body>
<div class="cover">
  <div class="cover-photo" role="img" aria-label="本棚が並ぶ薄暗い古い図書館の写真"></div>

  <p class="abs lead lead-ruby">生活の質</p>
  <p class="abs lead lead-1">あなたのQOLを</p>
  <p class="abs lead lead-2">大きく変える―</p>
  <p class="abs label label-1">ヴォルテノ大年譜</p>
  <p class="abs label-1-tail">など</p>
  <p class="abs label label-2">人類普遍の真理書</p>
  <p class="abs lead lead-3">ギュッと一冊にまとめました</p>

  <h1 class="title-block">
    <span class="abs title title-num">5</span>
    <span class="abs title title-tsu">つ</span>
    <span class="abs title title-no">の</span>
    <span class="abs title title-k1">航</span>
    <span class="abs title title-k2">路</span>
  </h1>

  <p class="abs role">メンタルトレーナー</p>
  <p class="abs author">RUNO</p>
  <p class="abs lead-4">あなたの</p>

  <div class="band"></div>
  <p class="abs red big-life">人生</p>
  <p class="abs navy tail-1">に足りないもの、</p>
  <p class="abs red trouble">困っていることの</p>
  <p class="abs red big-essence">本質</p>
  <p class="abs navy tail-2">がわかる!</p>

  <div class="gift-tag">読者限定<br>プレゼント</div>
  <p class="abs gift-text">これからも<br>成長する成功分野32選</p>
</div>
</body>
</html>
```